Welcome to the neighborhood Flyer

We want to create a postcard that welcomes our customers to the neighborhood. We want the front of the postcard to say "Welcome to the neighborhood" and have our store info:
Bramble 27 Wine & Spirits
412 Orchard Ln (19th Street)
(555) 204-7381
www.bramble27vino.example
Free neighborhood deliveries

On the back of the postcard we want to let our customers know of our Daily Specials.
Daily Specials 10% off at Bramble 27
Magnum Mondays : All 1.5L Wines
Tuscan Tuesdays : All 750ml Italian Wines
Wine-in-a-Box Wednesdays : All boxed Wines
Thirsty Thursdays : All 750ml Sparkling/Champagne
French Fridays : All 750ml French Wines
Surfin' Saturdays : All 750ml Californian Wines
South American & Spanish Sundays : All 750ml
We are thinking of black and white for both sides but we are open to any ideas and suggestions on color and wording!Thanks

Requirements
Must have
• Store info
Nice to have
• A Clean layout
• Nice and simple
Should not have
• Overcrowded wording

```html
<!DOCTYPE html>
<html lang="en">
<head>
<meta charset="utf-8">
<title>Bramble 27 Wine &amp; Spirits – Welcome Postcard</title>
<link href="https://fonts.googleapis.com/css2?family=Lobster&family=Fira+Sans:ital,wght@0,400;1,400;1,500;1,600&family=Oswald:wght@500&display=swap" rel="stylesheet">
<style>
  :root {
    --red: #e0223a;
    --dark: #2a2727;
    --ink: #222;
    --body: #444;
    --paper: #ffffff;
    --mist: #ececec;
    --bg: #f1f1f1;
  }
  * { margin: 0; padding: 0; box-sizing: border-box; }
  html, body { width: 1200px; height: 1200px; overflow: hidden; background: var(--bg); }
  .canvas { position: relative; width: 1200px; height: 1200px; }

  .card { position: absolute; background: var(--paper); overflow: hidden; }
  .card--front { left: 269px; top: 61px; width: 659px; height: 510px; }
  .card--back  { left: 269px; top: 610px; width: 662px; height: 513px; }

  .abs { position: absolute; }
  .script { font-family: "Lobster", cursive; }
  .sans { font-family: "Fira Sans", sans-serif; }

  /* front */
  .front-art { left: 0; top: 0; width: 659px; height: 280px; }
  .headline { left: 36px; top: 14px; color: var(--red); font-size: 52px; line-height: 1; }
  .subline { left: 36px; top: 64px; color: var(--ink); font-size: 24px; line-height: 1; }
  .brand { left: 34px; top: 128px; display: flex; align-items: center; gap: 10px; color: #fff;
           font-family: "Fira Sans", sans-serif; font-size: 34px; font-weight: 400; letter-spacing: .5px; }
  .brand-dot { width: 14px; height: 14px; border-radius: 50%; background: var(--red); }
  .delivery { left: 29px; top: 213px; color: var(--red); font-size: 16px; }

  .tiles { left: 23px; top: 310px; display: flex; gap: 9px; }
  .tile { width: 75px; height: 108px; box-shadow: 0 1px 3px rgba(0,0,0,.3); }
  .tile--rated { background: linear-gradient(160deg, #5a1712, #1e0a08); }
  .tile--picks { background: linear-gradient(160deg, #e0b36a, #8a5a22); }
  .tile--new   { background: linear-gradient(160deg, #8a6b3c, #3a2812); }
  .tile--pair  { background: linear-gradient(160deg, #6b1a20, #240608); }

  .established { right: 29px; top: 306px; color: var(--red); font-size: 30px; text-align: right; line-height: 1.1; }
  .about { right: 29px; top: 349px; width: 280px; text-align: right; font-style: italic;
           font-size: 12.6px; line-height: 15.8px; color: var(--body); }

  .front-footer { left: 0; top: 441px; width: 659px; height: 69px; }
  .front-footer-text { left: 0; top: 468px; width: 659px; text-align: center; color: #fff;
                       font-style: italic; font-size: 15px; }

  /* back */
  .storefront { left: 0; top: 0; width: 318px; height: 121px; background: linear-gradient(180deg, #3a3a3a, #8a8a8a 60%, #555); }
  .back-art { left: 0; top: 0; width: 662px; height: 513px; }
  .specials-title { left: 26px; top: 130px; color: #fff; font-family: "Oswald", sans-serif;
                    font-weight: 500; font-size: 14px; letter-spacing: -.1px; }
  .specials { left: 26px; top: 178px; list-style: none; font-style: italic; font-size: 12.4px;
              line-height: 16.6px; color: var(--ink); width: 290px; }
  .specials .day { color: var(--red); }
  .specials .day--lead { font-weight: 600; }
  .back-contact { left: 27px; top: 330px; color: #fff; font-style: italic; font-weight: 600;
                  font-size: 17px; line-height: 20px; }
  .stamp { left: 517px; top: 36px; width: 107px; height: 107px; background: #cfcfcf; }
</style>
</head>
<body>
<main class="canvas">

  <!-- Front of postcard -->
  <section class="card card--front">
    <svg class="abs front-art" viewBox="0 0 659 280" width="659" height="280" aria-hidden="true">
      <defs>
        <linearGradient id="band" x1="0" y1="0" x2="0" y2="1">
          <stop offset="0" stop-color="#3a3636"/><stop offset=".5" stop-color="#231f1f"/><stop offset="1" stop-color="#3a3636"/>
        </linearGradient>
        <linearGradient id="soft" x1="0" y1="0" x2="0" y2="1">
          <stop offset="0" stop-color="#ffffff"/><stop offset="1" stop-color="#e6e6e6"/>
        </linearGradient>
      </defs>
      <rect x="0" y="197" width="290" height="58" fill="url(#soft)"/>
      <polygon points="0,111 278,111 265,197 0,197" fill="url(#band)"/>
      <polygon points="0,108 279,108 278,112 0,112" fill="var(--red)"/>
      <polygon points="0,196 266,196 265,200 0,200" fill="var(--red)"/>
    </svg>
    <div class="abs" role="img" aria-label="Photo of the store interior with rows of wine racks and bottles"
         style="left:0;top:0;width:659px;height:248px;clip-path:polygon(290px 0,659px 0,659px 248px,242px 248px);background:linear-gradient(160deg,#d8cdb5 0%,#8a6a45 40%,#5a3e28 70%,#a08060 100%);"></div>
    <svg class="abs" style="left:0;top:0" width="659" height="290" viewBox="0 0 659 290" aria-hidden="true">
      <polygon points="283,0 291,0 243,248 235,248" fill="var(--red)"/>
      <path d="M0 254 H659 V279 H30 Q6 279 0 262 Z" fill="var(--red)"/>
      <path d="M0 252 Q4 276 30 281" stroke="var(--dark)" stroke-width="2" fill="none"/>
    </svg>

    <h1 class="abs headline script">Welcome</h1>
    <p class="abs subline script">to the neighborhood</p>
    <div class="abs brand"><span>Bramble 27</span><span class="brand-dot"></span></div>
    <p class="abs delivery script">Free neighborhood deliveries</p>

    <div class="abs tiles">
      <div class="tile tile--rated" role="img" aria-label="90+ rated wines: red wine glass artwork"></div>
      <div class="tile tile--picks" role="img" aria-label="Staff picks: corkscrew and bottle artwork"></div>
      <div class="tile tile--new" role="img" aria-label="New arrivals: white wine glass artwork"></div>
      <div class="tile tile--pair" role="img" aria-label="Food and wine pairing: bottle and glass artwork"></div>
    </div>

    <h2 class="abs established script">Established in 2010</h2>
    <p class="abs about sans">We are a large boutique store specializing in wine and spirits from all over the world. We're big, bold, and adventurous when it comes to discovering new wines and spirits.</p>

    <svg class="abs front-footer" viewBox="0 0 659 69" width="659" height="69" aria-hidden="true">
      <rect x="0" y="0" width="659" height="69" fill="var(--dark)"/>
      <path d="M0 8 H600 Q659 12 659 69 H0 Z" fill="var(--red)"/>
    </svg>
    <p class="abs front-footer-text sans">Spirits412 Orchard Ln (19th Street) | Call: (555) 204-7381 | Visit: www.bramble27vino.example</p>
  </section>

  <!-- Back of postcard -->
  <section class="card card--back">
    <div class="abs storefront" role="img" aria-label="Black and white photo of the storefront with its sign and window displays"></div>
    <svg class="abs back-art" viewBox="0 0 662 513" width="662" height="513" aria-hidden="true">
      <defs>
        <linearGradient id="panel" x1="0" y1="0" x2="0" y2="1">
          <stop offset="0" stop-color="#ffffff"/><stop offset="1" stop-color="#dedede"/>
        </linearGradient>
      </defs>
      <rect x="0" y="121" width="318" height="190" fill="url(#panel)"/>
      <path d="M0 121 H318 V125 H283 Q283 161 245 161 H0 Z" fill="var(--red)"/>
      <rect x="0" y="428" width="0" height="0"/>
      <rect x="0" y="307" width="318" height="5" fill="var(--dark)"/>
      <path d="M0 312 H318 V366 Q318 421 263 421 H83 V513 H0 Z" fill="var(--red)"/>
    </svg>
    <p class="abs specials-title">Daily Specials 10% off at Bramble 27 Magnum</p>
    <ul class="abs specials sans">
      <li><span class="day day--lead">Mondays:</span> All 1.5L WinesTuscan</li>
      <li><span class="day">Tuesdays:</span> All 750ml Italian WinesWine-in-a-Box</li>
      <li><span class="day">Wednesdays:</span> All boxed WinesThirsty</li>
      <li><span class="day">Thursdays:</span> All 750ml Sparkling/ChampagneFrench</li>
      <li><span class="day">Fridays:</span> All 750ml French WinesSurfin'</li>
      <li><span class="day">Saturdays:</span> All 750ml Californian WinesSouth American &amp; Spanish Sundays : All 750ml</li>
    </ul>
    <p class="abs back-contact sans">Spirits412 Orchard Ln (19th Street)<br>Call: (555) 204-7381<br>Visit: www.bramble27vino.example</p>
    <div class="abs stamp" aria-label="Stamp area"></div>
  </section>

</main>
</body>
</html>
```